Design a book cover for "The Ledgerkeeper's Yarn"

We need a book cover for a book titled "The Ledgerkeeper's Yarn" The subtitle is "How Machines Permit a Shared Dividend, the Close of Wage Levies, and an Even Treasury"
You can use one of the attached files of cover art, or come up with your own art - designer's choice!
Author's Name is Derek Halvorn
We'd like the copy in the attached file "Back Cover" on the back cover, along with the copy in "About the Author" and the author's photo on the back cover.
Updates

Project Deadline Extended Reason: The deadline has been extended to give time for designers to respond to comments. Feel free to submit designs that do not use the cover art graphics attached to the brief - that art was meant as a suggestion. Added Sunday, January 15, 2017

Target Market(s)

Layperson

Font styles to use
Sans Serif

Colors
0456a4
3176b5
85abd2
0293ce
33a6d7
85cae6
1b1b1b
474747
919191

Requirements
Nice to have
• We'd like to see how the horse and rider would look on the front cover. The attached file, "Wendlow Option", is a rough sketch. The artist is refining it, adding color, and will have the rider carrying modern technology instead of scrolls.
• We are open to all colors, but have indicated some colors we like.

```html
<!DOCTYPE html>
<html lang="en">
<head>
<meta charset="utf-8">
<title>The Ledgerkeeper's Yarn — Derek Halvorn</title>
<link rel="stylesheet" href="https://fonts.googleapis.com/css2?family=League+Gothic&family=Montserrat:wght@700&display=swap">
<style>
  :root {
    --backdrop: #e2e2e2;
    --paper: #ffffff;
    --plum: #4a3466;
    --plum-light: #5c4579;
    --plum-dark: #3a2753;
    --emblem-glow: rgba(255, 255, 255, 0.14);
    --ink: #1b1b1b;
    --white: #ffffff;
  }
  * { margin: 0; padding: 0; box-sizing: border-box; }
  html, body {
    width: 900px;
    height: 1200px;
    overflow: hidden;
    background: var(--backdrop);
  }
  .cover {
    position: absolute;
    left: 38px;
    top: 36px;
    width: 824px;
    height: 1066px;
    background: var(--paper);
    box-shadow: 3px 4px 6px rgba(0, 0, 0, 0.28);
    overflow: hidden;
  }
  .cover-art {
    position: absolute;
    inset: 0 0 auto 0;
    height: 770px;
    background:
      radial-gradient(ellipse at 28% 62%, var(--plum-light) 0%, transparent 55%),
      radial-gradient(ellipse at 88% 30%, var(--plum-dark) 0%, transparent 50%),
      var(--plum);
  }
  .emblem {
    position: absolute;
    left: 236px;
    top: 104px;
    width: 330px;
    height: 290px;
    border-radius: 50%;
    background: radial-gradient(ellipse at center, var(--emblem-glow) 0%, transparent 70%);
  }
  .title {
    position: absolute;
    left: 0;
    right: 0;
    top: 418px;
    text-align: center;
    color: var(--white);
    font-family: "League Gothic", "Oswald", sans-serif;
    font-weight: 400;
    text-transform: uppercase;
    line-height: 1;
  }
  .title-lead {
    display: block;
    font-size: 76px;
    letter-spacing: 0;
  }
  .title-main {
    display: block;
    margin-top: -2px;
    font-size: 290px;
    line-height: 0.84;
    letter-spacing: 1px;
  }
  .subtitle {
    position: absolute;
    left: 0;
    right: 0;
    top: 806px;
    text-align: center;
    color: var(--ink);
    font-family: "Montserrat", sans-serif;
    font-weight: 700;
    text-transform: uppercase;
  }
  .subtitle-lead {
    display: block;
    font-size: 20px;
    letter-spacing: 0.3px;
  }
  .subtitle-points {
    display: flex;
    justify-content: center;
    gap: 17px;
    margin-top: 22px;
    font-size: 16px;
    letter-spacing: 0.2px;
    list-style: none;
  }
  .subtitle-points li::before {
    content: "•";
    margin-right: 17px;
  }
  .author {
    position: absolute;
    left: 0;
    right: 0;
    top: 904px;
    text-align: center;
    color: var(--ink);
    font-family: "League Gothic", "Oswald", sans-serif;
    font-size: 96px;
    line-height: 1;
    letter-spacing: 1px;
    text-transform: uppercase;
  }
</style>
</head>
<body>
  <article class="cover">
    <div class="cover-art" role="img" aria-label="Purple-toned photograph of stacked coins, a pen and printed financial pages">
      <div class="emblem" role="img" aria-label="Line illustration of dollar tags linked to a cloud by circuit lines"></div>
      <h1 class="title">
        <span class="title-lead">The Ledgerkeeper's</span>
        <span class="title-main">Yarn</span>
      </h1>
    </div>

    <h2 class="subtitle">
      <span class="subtitle-lead">How Machines Permit</span>
      <ul class="subtitle-points">
        <li>A Shared Dividend</li>
        <li>The Close of Wage Levies</li>
        <li>An Even Treasury</li>
      </ul>
    </h2>

    <p class="author">Derek Halvorn</p>
  </article>
</body>
</html>
```